A NEW UPDATED VERSION OF A 4"X9" RACK CARD

A NEW UPDATED VERSION OF A RACK CARD, THIS CARD IS 5 YEARS OLD AND WE WANT SOMETHING NEW AND FRESH AND MORE UPDATED TO TODAY. MARKET TO A YOUNGER CROWD. USE THE ATTACHED RACK CARD FOR THE INFO AND VERBAGE AND LOGO TO BE USED. DO NOT USE THE PICTURE OF THE BUILDIING, don't use the picture of the 2 guys. USED THE ATTACHED POST CARDS AS COLORS AND REFERENCE.

Target Market(s)

25-45

Industry/Entity Type

HOME INSPECTIONS

```html
<!DOCTYPE html>
<html lang="en">
<head>
<meta charset="UTF-8">
<title>BrightKey Home Inspections – Rack Card</title>
<link href="https://fonts.googleapis.com/css2?family=Roboto:wght@400;500;700;900&display=swap" rel="stylesheet">
<style>
  :root {
    --red: #d71f26;
    --blue: #1b4b9b;
    --navy: #173f8c;
    --steel-light: #eceef0;
    --steel: #c9cdd2;
    --ink: #333;
    --page: #d9d9d9;
    --white: #ffffff;
  }
  * { box-sizing: border-box; margin: 0; padding: 0; }
  html, body { width: 1200px; height: 802px; overflow: hidden; }
  body {
    background: var(--page);
    font-family: 'Roboto', sans-serif;
    position: relative;
  }
  .rack-card {
    position: absolute;
    left: 431px; top: 21px;
    width: 338px; height: 760px;
    background: var(--white);
    box-shadow: 0 6px 20px rgba(0,0,0,.18);
    overflow: hidden;
    text-align: center;
  }
  .plate-texture {
    position: absolute; inset: 0 0 auto 0; height: 470px;
    background: linear-gradient(180deg, var(--steel) 0%, var(--steel-light) 55%, var(--white) 100%);
  }
  .content { position: relative; }
  .brand {
    height: 250px;
    display: flex; flex-direction: column; align-items: center; justify-content: center; gap: 12px;
  }
  .brand-dot {
    width: 44px; height: 44px; border-radius: 50%; background: var(--red);
  }
  .brand-name {
    font-weight: 900; font-size: 26px; line-height: 1.1; color: var(--blue);
    text-transform: uppercase; width: 260px;
  }
  .eyebrow {
    margin-top: 14px;
    color: var(--red); font-size: 11px; font-weight: 500; letter-spacing: .3px;
  }
  .headline {
    color: var(--blue); font-weight: 900; font-size: 26px; line-height: 1.08;
    text-transform: uppercase; margin-top: 2px;
  }
  .rule { width: 220px; height: 1px; background: var(--red); margin: 12px auto 12px; }
  .subhead { color: var(--blue); font-size: 16px; font-weight: 500; }
  .services-label { color: var(--red); font-size: 11px; margin-top: 10px; }
  .services {
    display: grid; grid-template-columns: repeat(3, 96px); gap: 16px 12px;
    justify-content: center; margin-top: 14px;
  }
  .service {
    height: 92px; background: var(--white);
    box-shadow: 2px 3px 6px rgba(0,0,0,.16);
    display: flex; flex-direction: column; align-items: center; padding-top: 10px;
  }
  .service-icon {
    width: 40px; height: 40px; border-radius: 50%; background: var(--red);
    display: flex; align-items: center; justify-content: center;
    box-shadow: 0 2px 4px rgba(0,0,0,.25);
  }
  .service-icon svg { width: 22px; height: 22px; fill: none; stroke: var(--white); stroke-width: 1.6; stroke-linejoin: round; stroke-linecap: round; }
  .service-name { font-size: 9px; font-weight: 700; color: var(--ink); line-height: 1.2; margin-top: 8px; }
  .cta { position: absolute; left: 0; right: 0; top: 640px; height: 56px; }
  .phone-bar {
    position: absolute; left: 150px; right: 0; top: 0; height: 40px;
    background: var(--red); color: var(--white);
    font-weight: 700; font-size: 14px;
    display: flex; align-items: center; justify-content: center; gap: 6px;
  }
  .phone-bar svg { width: 12px; height: 12px; fill: var(--white); }
  .tagline {
    position: absolute; left: 10px; top: 4px; width: 160px; height: 52px;
    background: var(--white); border: 1.5px solid var(--red);
    color: var(--red); text-align: left; padding: 5px 0 0 12px;
  }
  .tagline strong { display: block; font-size: 24px; font-weight: 900; line-height: 1; }
  .tagline span { display: block; font-size: 12px; font-weight: 500; margin-top: 2px; }
  .footer-rule { position: absolute; left: 0; right: 0; top: 704px; height: 3px; background: var(--red); }
  .footer {
    position: absolute; left: 0; right: 0; top: 710px; bottom: 0;
    background: var(--navy); color: var(--white); font-size: 11px;
    display: flex; align-items: center; justify-content: center; gap: 5px;
  }
  .footer svg { width: 11px; height: 11px; fill: none; stroke: var(--white); stroke-width: 1.3; }
</style>
</head>
<body>
<main class="rack-card">
  <div class="plate-texture" role="img" aria-label="Brushed diamond-plate steel texture"></div>
  <div class="content">
    <header class="brand">
      <div class="brand-dot"></div>
      <div class="brand-name">BrightKey Home Inspections</div>
    </header>
    <p class="eyebrow">★ YOUR TRUSTED ★</p>
    <h1 class="headline">Home Inspection<br>Expert</h1>
    <div class="rule"></div>
    <h2 class="subhead">MULTI-INSPECTOR FIRM</h2>
    <p class="services-label">Our Services</p>
    <section class="services">
      <div class="service">
        <div class="service-icon"><svg viewBox="0 0 24 24"><path d="M4 11 12 4l8 7M6 10v10h12V10M10 20v-6h4v6"/></svg></div>
        <p class="service-name">Home<br>Inspections</p>
      </div>
      <div class="service">
        <div class="service-icon"><svg viewBox="0 0 24 24"><path d="M4 9l2-5h12l2 5H4zM5 9v11h14V9M10 20v-5h4v5"/></svg></div>
        <p class="service-name">Commercial<br>Inspections</p>
      </div>
      <div class="service">
        <div class="service-icon"><svg viewBox="0 0 24 24"><path d="M4 4h8l8 8-8 8-8-8z"/><circle cx="8.5" cy="8.5" r="1.5"/></svg></div>
        <p class="service-name">Pre-listing<br>Inspections</p>
      </div>
      <div class="service">
        <div class="service-icon"><svg viewBox="0 0 24 24"><path d="M9 9V6a3 3 0 1 0-3 3h12a3 3 0 1 0-3-3v12a3 3 0 1 0 3-3H6a3 3 0 1 0 3 3V9"/></svg></div>
        <p class="service-name">4-Point<br>Inspections</p>
      </div>
      <div class="service">
        <div class="service-icon"><svg viewBox="0 0 24 24"><path d="M4 20h16M6 20V11h5v9M11 20V6h7v14M14 3v3M13 9h2M13 12h2M13 15h2"/></svg></div>
        <p class="service-name">Builder's Warranty<br>Inspections</p>
      </div>
      <div class="service">
        <div class="service-icon"><svg viewBox="0 0 24 24"><path d="M3 9h11a3 3 0 1 0-3-3M3 13h15a3 3 0 1 1-3 3M3 17h7"/></svg></div>
        <p class="service-name">Wind<br>Mitigations</p>
      </div>
    </section>
  </div>
  <section class="cta">
    <div class="phone-bar">
      <svg viewBox="0 0 24 24"><path d="M6.6 10.8a15 15 0 0 0 6.6 6.6l2.2-2.2c.3-.3.7-.4 1-.2 1.1.4 2.3.6 3.6.6.6 0 1 .4 1 1V20c0 .6-.4 1-1 1A17 17 0 0 1 3 4c0-.6.4-1 1-1h3.5c.6 0 1 .4 1 1 0 1.3.2 2.5.6 3.6.1.3 0 .7-.2 1z"/></svg>
      <span>1-800-555-0142</span>
    </div>
    <div class="tagline"><strong>INSPECTING</strong><span>FOR THE UNEXPECTED</span></div>
  </section>
  <div class="footer-rule"></div>
  <footer class="footer">
    <svg viewBox="0 0 12 12"><circle cx="6" cy="6" r="5"/><path d="M1 6h10M6 1c2 2 2 8 0 10M6 1c-2 2-2 8 0 10"/></svg>
    <span>brightkeyinspections.com</span>
  </footer>
</main>
</body>
</html>
```